Business Card Design Project

Hello
I want a Simple Business card that uses the company logo that is easily reasonable but looks professional as I am an IT Services company and would look to share these cards with prospective clients.
The details are:
Kestrel Arc Solutions
14 Morrow Lane
Birmingham
B7 4QX
Telephone 0845 217 6640
I would like my name Oliver Hastings and my title Director on the card.
Target Market(s)
IT Professionals
Industry/Entity Type
Business

```html
<!DOCTYPE html>
<html lang="en">
<head>
<meta charset="utf-8">
<title>Kestrel Arc Solutions – Business Card</title>
<link rel="stylesheet" href="https://fonts.googleapis.com/css2?family=Arimo:wght@400;700&display=swap">
<style>
  :root {
    --backdrop: #e6e6e4;
    --card: #ffffff;
    --leaf-green: #8cc63f;
    --ink: #2b2b2b;
    --band-text: #ffffff;
    --font-main: "Arimo", Arial, sans-serif;
  }
  * { box-sizing: border-box; margin: 0; padding: 0; }
  html, body {
    width: 1200px;
    height: 741px;
    overflow: hidden;
  }
  body {
    background: var(--backdrop);
    font-family: var(--font-main);
    display: flex;
    align-items: center;
    justify-content: center;
  }
  .business-card {
    position: relative;
    width: 760px;
    height: 460px;
    background: var(--card);
    border-radius: 16px;
    box-shadow: 0 10px 30px rgba(0, 0, 0, 0.18);
    overflow: hidden;
  }
  .brand {
    position: absolute;
    left: 56px;
    top: 150px;
    display: flex;
    align-items: center;
    gap: 14px;
  }
  .brand-dot {
    width: 50px;
    height: 50px;
    border-radius: 50%;
    background: var(--leaf-green);
  }
  .brand-name {
    font-size: 34px;
    font-weight: 700;
    color: var(--ink);
    letter-spacing: -0.5px;
  }
  .address {
    position: absolute;
    right: 56px;
    top: 48px;
    text-align: right;
    font-style: normal;
    font-size: 25px;
    line-height: 1.18;
    color: var(--ink);
  }
  .address .street { color: var(--leaf-green); }
  .contact-band {
    position: absolute;
    left: 0;
    right: 0;
    top: 246px;
    height: 132px;
    background: var(--leaf-green);
    padding: 26px 56px 0;
    font-size: 25px;
    line-height: 1.25;
  }
  .contact-name { color: var(--band-text); }
  .contact-phone { color: var(--band-text); }
  .contact-phone .label { color: var(--ink); }
</style>
</head>
<body>
  <article class="business-card">
    <div class="brand">
      <span class="brand-dot"></span>
      <span class="brand-name">Kestrel Arc</span>
    </div>
    <address class="address">
      <div class="company">Kestrel Arc Solutions</div>
      <div class="street">14 Morrow Lane</div>
      <div class="city">Birmingham</div>
      <div class="postcode">B7 4QX</div>
    </address>
    <div class="contact-band">
      <p class="contact-name">Oliver Hastings (Director)</p>
      <p class="contact-phone"><span class="label">phone</span> 0845 217 6640</p>
    </div>
  </article>
</body>
</html>
```